Smart, Classy, Conservative looking Legal Letterhead

I need a letterhead that when you look at it it "says to you " this is a well established law firm with very smart lawyers, which will one day be appearing before the Supreme Court of the USA. All information about the Law firm should appear at the top of the page. please no information in the footer.

Industry/Entity Type

Legal

Requirements
Must have
• The name of the law firm, both addresses, phone number and fax,, The names of the attorneys, the website.
• Fields that get changed such as the date, VIA, Address of who the letter is going to,
• Re, Index,
• should have a clean neat look, sleek
Nice to have
• some color would be nice. A logo of some sort could be nice as well. Maybe a single S or interlocking B's For Brevik and Brevik.
Should not have
• not too modern looking.

```html
<!DOCTYPE html>
<html lang="en">
<head>
<meta charset="utf-8">
<title>Brevik &amp; Brevik, LLP — Letterhead</title>
<link href="https://fonts.googleapis.com/css2?family=Crimson+Text:wght@400;600;700&family=Arimo:wght@400;700&family=Pinyon+Script&display=swap" rel="stylesheet">
<style>
  :root {
    --backdrop: #e9e6e1;
    --paper: #ffffff;
    --ink: #111111;
    --ink-soft: #7a7a7a;
    --brand-blue: #1b8fd0;
    --rule: #3d3d3d;
  }
  * { margin: 0; padding: 0; box-sizing: border-box; }
  html, body {
    width: 1200px; height: 1000px; overflow: hidden;
    background: var(--backdrop);
  }
  body { position: relative; font-family: "Crimson Text", Georgia, serif; color: var(--ink); }

  .letterhead {
    position: absolute; left: 300px; top: 30px;
    width: 612px; height: 933px;
    background: var(--paper);
    box-shadow: 0 2px 10px rgba(0,0,0,0.18);
  }
  .letterhead > * { position: absolute; }

  /* Firm identity */
  .firm-identity { left: 58px; top: 67px; display: flex; align-items: flex-start; gap: 6px; }
  .firm-mark { width: 30px; height: 36px; background: var(--brand-blue); }
  .firm-name-block { line-height: 11px; padding-top: 13px; }
  .firm-name { font-size: 14px; color: var(--brand-blue); letter-spacing: 0.2px; text-transform: uppercase; }
  .firm-tagline { font-size: 14px; color: var(--ink); text-transform: uppercase; }

  /* Main office contact */
  .main-office { left: 348px; top: 65px; width: 204px; font-size: 8.6px; line-height: 11.5px; text-transform: uppercase; font-style: normal; }
  .main-office .row { display: flex; justify-content: space-between; }
  .main-office .online { margin-top: 7px; }

  /* Attorney roster */
  .attorney-roster { left: 59px; top: 141px; font-size: 8.4px; line-height: 10.6px; text-transform: uppercase; list-style: none; }
  .attorney-roster .note { padding-left: 9px; }

  /* Branch office */
  .branch-office { left: 432px; top: 139px; font-family: "Arimo", Arial, sans-serif; font-size: 7.6px; line-height: 11px; font-weight: 700; font-style: normal; }

  /* Variable letter fields */
  .letter-date { left: 59px; top: 213px; font-size: 13px; font-weight: 700; }
  .delivery-method { right: 63px; top: 214px; font-size: 13.5px; text-transform: uppercase; }

  .recipient { left: 60px; top: 253px; font-size: 14.2px; line-height: 15px; font-style: normal; }

  .reference { left: 59px; top: 390px; font-size: 15px; line-height: 15px; }
  .reference .field { display: flex; }
  .reference .field-label { width: 72px; }

  .letter-body { left: 59px; top: 461px; width: 458px; font-size: 13.4px; line-height: 15px; color: var(--ink-soft); }
  .letter-body .indent { text-indent: 36px; }

  .signature-line { left: 66px; top: 622px; font-family: "Pinyon Script", cursive; font-size: 29px; color: var(--ink); }
  .sign-off { left: 68px; top: 675px; font-size: 13px; font-weight: 700; line-height: 22px; }

  .base-rule { left: 90px; top: 886px; width: 430px; height: 3px; background: var(--rule); }
</style>
</head>
<body>
  <main class="letterhead">
    <div class="firm-identity">
      <span class="firm-mark" aria-hidden="true"></span>
      <div class="firm-name-block">
        <div class="firm-name">Brevik &amp; Brevik, LLP</div>
        <div class="firm-tagline">Attorneys at Law</div>
      </div>
    </div>

    <address class="main-office">
      <div class="row"><span>48 Harbor Street</span><span>Tel: 555-201-4470</span></div>
      <div class="row"><span>New York, New York 10005</span><span>Fax: 555-201-4471</span></div>
      <div class="online">david.brevik@breviklegal.com<br>www.brevikconsumerlaw.com</div>
    </address>

    <ul class="attorney-roster">
      <li>Martin Brevik, Esq.</li>
      <li>David A. Brevik, Esq.</li>
      <li>Eleanor Whitcombe, Esq.</li>
      <li>Paul T. Ardell, Esq.*</li>
      <li class="note">*Admitted in NY &amp; MA</li>
    </ul>

    <address class="branch-office">
      <div>WESTCHESTER OFFICE</div>
      <div>217 Orchard Lane</div>
      <div>Fairhollow, New York 10599</div>
    </address>

    <div class="letter-date">October 14, 2014</div>
    <div class="delivery-method">Via Swiftpost</div>

    <address class="recipient">
      Hon. Fake Judge Name Here<br>
      United States District Court, E.D.N.Y.<br>
      400 Courthouse Square<br>
      Courtroom XXXXX<br>
      Eastbrook, NY 11700-0000
    </address>

    <div class="reference">
      <div class="field"><span class="field-label">Re:</span><span>XXXXXXXXXXXXXXXXXXX</span></div>
      <div class="field"><span class="field-label">Index:</span><span>XXXXXXXX</span></div>
    </div>

    <div class="letter-body">
      <p>Your Honor:</p>
      <p class="indent">Pursuant to Your Honor’s Individual Practices Rule III(C)(3), enclosed<br>please find a courtesy copy of Plaintiff’s Revised Yadda Yadda Yadda.</p>
      <p>Respectfully,</p>
    </div>

    <div class="signature-line">Signature</div>
    <div class="sign-off">Respectfully,<br>David A. Brevik</div>

    <div class="base-rule" aria-hidden="true"></div>
  </main>
</body>
</html>
```